Up and coming Australian Systems Integrator needs a proposal template refresh

We need to update our proposal template and are looking for a fresh, modern, simple and elegant proposal template. We'd like to keep our existing logos if possible.
NovaLink is a privately owned company operating since 2006. Offices and technical staff located in Quarry Bay and Ridgeford
Sustained, profitable growth year on year
Velnet strategic partner
Velnet Advanced Enterprise Network Architecture Specialisation
Velnet Advanced Security Architecture Specialisation
Velnet Advanced Collaboration Architecture Specialisation
Velnet Advanced Unified Computing Technology Specialisation
Velnet Advanced Data Centre Architecture Specialisation (in progress)
Velnet Gold Partner – Expect 2H2018
As well as being a Velnet partner we have a well established stable of other vendors such as Brakwell, Tavrimo, Harbourtone, DPQ, Moltrane Dialogic, Zell, SkyTrover, VoLERNA Drift)
We are a top two provider of Velnet product/services in the Victorian healthcare sector.
Updates
Please feel free to use different colors and fonts as we feel the existing ones look dated.

```html
<!DOCTYPE html>
<html lang="en">
<head>
<meta charset="utf-8">
<title>NovaLink Proposal Template</title>
<link href="https://fonts.googleapis.com/css2?family=Open+Sans:wght@300;400;600;700&display=swap" rel="stylesheet">
<style>
:root{
  --backdrop:#a2a2a2;
  --navy:#1b3466;
  --slate:#6e7987;
  --accent:#1f5fa8;
  --ink:#3a3a3a;
  --rule:#9aa8c2;
  --cell:#dde8f5;
  --cell-strong:#b9d6f1;
  --paper:#ffffff;
}
*{margin:0;padding:0;box-sizing:border-box}
html,body{width:1200px;height:1200px;overflow:hidden}
body{background:var(--backdrop);font-family:"Open Sans",Arial,sans-serif;color:var(--ink);position:relative}
.page{position:absolute;width:259px;height:366px;background:var(--paper);box-shadow:2px 3px 5px rgba(0,0,0,.28);overflow:hidden}
.c1{left:23px}.c2{left:321px}.c3{left:618px}.c4{left:918px}
.r1{top:32px}.r2{top:422px}.r3{top:810px}

/* shared header */
.page-head{position:absolute;left:29px;right:27px;top:16px;border-top:1px dotted var(--rule);border-bottom:1px dotted var(--rule);padding:4px 0 3px;text-align:center;font-size:8.6px;font-weight:400;letter-spacing:.2px;color:#222}
.page-body{position:absolute;left:29px;right:27px;top:46px}
.txt{font-size:3.9px;line-height:1.7;margin-bottom:4px;color:var(--ink)}
.txt.lead{color:var(--accent)}
.sub{font-size:6.6px;font-weight:600;color:var(--accent);margin:4px 0 2px}
.mini{font-size:3.8px;color:var(--accent);margin-bottom:1px}

/* shared footer */
.page-foot{position:absolute;left:0;right:0;bottom:10px;height:5px}
.page-foot .bar{position:absolute;left:0;width:190px;top:0;height:5px;background:var(--navy);color:#fff;font-size:3.3px;line-height:5px;padding-left:24px}
.page-foot .wedge{position:absolute;left:190px;top:0;width:10px;height:5px}
.page-foot .brand{position:absolute;left:205px;top:-1px;font-size:5px;font-weight:600;color:var(--navy);letter-spacing:.3px}
.page-foot .num{position:absolute;right:0;width:20px;top:0;height:5px;background:var(--slate);color:#fff;font-size:3.2px;line-height:5px;text-align:center}

/* cover */
.cover svg,.back svg{position:absolute;left:0;top:0}
.cover-title{position:absolute;left:0;right:0;top:48px;text-align:center;color:#fff;font-weight:700;font-size:12.6px;line-height:1.2}
.cover-sub{position:absolute;left:0;right:0;top:97px;text-align:center;color:#fff;font-weight:600;font-size:8.8px}
.cover-date{position:absolute;left:26px;top:336px;font-size:7px;font-weight:700;color:var(--navy)}
.wordmark{position:absolute;display:flex;align-items:center;gap:4px;color:var(--navy);font-weight:600;letter-spacing:.6px}
.wordmark i{display:block;background:var(--slate)}
.cover .wordmark{left:136px;top:330px;font-size:12px}
.cover .wordmark i{width:9px;height:9px}

/* revision page */
.rev{position:absolute;left:36px;top:45px;width:188px;border-collapse:collapse}
.rev th{font-size:3.4px;font-weight:400;color:var(--accent);text-align:left;padding:1px 2px;border:1px solid #cfd6e0;height:9px}
.rev td{border:1px solid #cfd6e0;height:11px;background:#f0f0f0}
.rev td:first-child,.rev td:nth-child(3){background:#fff}
.legal{position:absolute;left:53px;top:310px;width:182px;font-size:3.3px;line-height:1.55}
.legal .rights{border-left:1px solid var(--navy);padding-left:2px;color:var(--accent);margin-bottom:6px;height:22px}

/* toc */
.toc-heading{font-size:7px;font-weight:700;color:var(--navy);margin-bottom:7px}
.toc li{list-style:none;display:flex;font-size:3.9px;line-height:2.25}
.toc .dots{flex:1;border-bottom:1px dotted #888;margin:0 3px 3px}

/* vision */
.mission{display:flex;align-items:center;background:var(--navy);height:22px;margin-bottom:6px}
.mission .icon{width:26px;height:22px;background:#555;display:flex;align-items:center;justify-content:center;flex:none}
.mission p{color:#fff;font-size:4.2px;line-height:1.35;padding:0 5px}

/* photos */
.photo{position:absolute;background:linear-gradient(135deg,#6f8fb4 0%,#37506f 45%,#20222a 100%)}

/* tables */
.grid{width:100%;border-collapse:separate;border-spacing:0 1px;font-size:3.6px;margin:5px 0}
.grid th{background:var(--navy);color:#fff;font-weight:600;height:7px;padding:0 3px}
.grid td{background:var(--cell);height:8px;padding:0 3px;text-align:center}
.grid td:first-child{text-align:left}
.grid tr.phase td{background:var(--cell-strong);color:var(--accent);font-weight:600}
.grid tr.total td{font-weight:700}
.grid tr.grand td{background:#2a8fe0;color:#fff;font-weight:600}

.bullets li{list-style:none;font-size:3.8px;line-height:1.75;margin-bottom:3px;padding-left:4px;position:relative}
.bullets li:before{content:"";position:absolute;left:0;top:2.5px;width:2px;height:2px;background:var(--navy)}
.bullets ul{margin:2px 0 0 10px}
.bullets ul li{color:var(--accent);margin-bottom:1px}
.bullets ul li:before{background:none;border-left:2px solid var(--accent);border-top:1px solid transparent;border-bottom:1px solid transparent;width:0;height:0}

/* back cover */
.back .wordmark{left:55px;top:330px;font-size:9px}
.back .wordmark i{width:7px;height:7px}
.contact{position:absolute;left:128px;top:302px;font-size:3.5px;line-height:1.5;padding-left:4px;border-left:1px solid #ccc;height:50px}
.contact .line{display:flex;align-items:center;gap:2px}
.contact .dot{width:4px;height:4px;border-radius:50%;background:var(--navy);display:inline-block}
</style>
</head>
<body>

<!-- Cover -->
<section class="page c1 r1 cover">
  <svg width="259" height="366" viewBox="0 0 259 366">
    <polygon points="0,0 259,0 259,204 0,296" fill="#1b3466"/>
    <polygon points="0,296 259,204 259,248" fill="#6e7987"/>
  </svg>
  <h1 class="cover-title">LOREM IPSUM IS SIMPLY<br>DUMMY HAS BEEN</h1>
  <p class="cover-sub">Lorem Ipsum Is Simply Dummy Has Been</p>
  <p class="cover-date">05.09.2018</p>
  <div class="wordmark"><i></i>NOVALINK</div>
</section>

<!-- Revision history -->
<section class="page c2 r1">
  <table class="rev">
    <tr><th style="width:30px">Version #</th><th style="width:78px">Purpose / Changes</th><th style="width:52px">Author</th><th>Date</th></tr>
    <tr><td></td><td></td><td></td><td></td></tr>
    <tr><td></td><td></td><td></td><td></td></tr>
    <tr><td></td><td></td><td></td><td></td></tr>
    <tr><td></td><td></td><td></td><td></td></tr>
    <tr><td></td><td></td><td></td><td></td></tr>
  </table>
  <div class="legal">
    <p class="rights">Copyright © 2018 xxxxx Limited<br>All Rights Reserved</p>
    <p>No part of the contents of this document may be reproduced or distributed in any form or by any means without the prior written permission of xxx Limited</p>
  </div>
</section>

<!-- Table of contents -->
<section class="page c3 r1">
  <h2 class="page-head">TABLE OF CONTENTS</h2>
  <div class="page-body" style="top:51px">
    <p class="toc-heading">Contents</p>
    <ul class="toc">
      <li>Table of Contents<span class="dots"></span>01</li>
      <li>Executive Summary<span class="dots"></span>02</li>
      <li>Our Understanding of Your Needs<span class="dots"></span>02</li>
      <li>Our Recommendations<span class="dots"></span>03</li>
      <li>Our Approach<span class="dots"></span>05</li>
      <li>Budget and Timeframe<span class="dots"></span>07</li>
      <li>Appendix A: About Mallow Creek<span class="dots"></span>10</li>
      <li>Appendix B: Selected Client List<span class="dots"></span>10</li>
      <li>Appendix C: Our Capabilities<span class="dots"></span>11</li>
      <li>Appendix D: Our Process<span class="dots"></span>12</li>
    </ul>
  </div>
  <footer class="page-foot"><div class="bar">www.NovaLink.net.au</div><svg class="wedge" viewBox="0 0 10 5"><polygon points="0,0 10,0 5,5 0,5" fill="#1b3466"/></svg><span class="brand">NOVALINK</span><span class="num">01</span></footer>
</section>

<!-- Vision -->
<section class="page c4 r1">
  <h2 class="page-head">VISION</h2>
  <div class="page-body" style="left:26px;right:23px">
    <div class="mission">
      <div class="icon"><svg width="14" height="14" viewBox="0 0 14 14"><circle cx="7" cy="7" r="6" fill="none" stroke="#fff" stroke-width="1.2"/><circle cx="7" cy="7" r="3.5" fill="none" stroke="#fff" stroke-width="1.2"/><circle cx="7" cy="7" r="1.2" fill="#fff"/></svg></div>
      <p>Tallyo's mission is to help and support the self-employed and small business owners with their administrative tasks so they can focus on what matters – their business.</p>
    </div>
    <p class="txt lead">Administrative tasks are cumbersome, time-consuming and often prevent small owners from focusing their time and energy on their business and their customers. They can also be extremely stressful and nerve-wracking for those attempting these tasks for the first time.</p>
    <p class="txt" style="text-align:center">At Tallyo, we envisage accounting for the self-employed and small business owners as being <span style="color:var(--accent)">automated and decentralized</span></p>
    <p class="txt">Accounting can and should be done automatically. By connecting to all sources of accounting data such as bank accounts, payment systems, e-commerce websites, and invoicing systems, Tallyo AI automatically completes these tasks, which would take hours to do manually. Bookings are created automatically and fully completed. Financial statements are available within a couple of clicks, and after analysing your data, Tallyo AI will offer you tips to improve your financial stability.</p>
    <p class="txt">What may seem like a pipedream to the millions of self-employed who struggle with their admin, is already a reality. Now is the time to join Tallyo on its mission to transform the world of bookkeeping through the power of AI.</p>
    <p class="sub">The Tallyo model</p>
    <p class="txt">Tallyo is based on an innovative license model that uses Token-as-a-License (TaaL). The token represents lifelong software license for Tallyo solutions. The Pre-ICO token sales will enable Tallyo to complete its development of Tallyo AI to deliver fully automatic bookkeeping.</p>
    <p class="txt">The Pre-ICO token sale will also pave the way for a future Tallyo ICO. Tallyo will launch accounting on the blockchain and ensure your accounting data is comprehensive and private, but available everywhere within your preferred apps. It will empower you to manage your data as you see fit in a fully decentralized way. Furthermore, a new range of business apps will connect to Tallyo to provide you with leading edge business data access to ensure you have the best available data at your fingertips.</p>
    <p class="txt">Tallyo supports strong data ownership laws that truly protect individuals and ensure they have complete ownership of their data. Through decentralisation Tallyo helps to ensure you always have full ownership of your data to decide how it should be used.</p>
    <p class="txt">To find out more about the Tallyo AI project, and the Tallyo TaaL or if you are interested in purchasing Tallyo TaaL, please register with your email at <span style="color:var(--accent);text-decoration:underline">www.tallyo.example/en/ico</span></p>
  </div>
  <footer class="page-foot"><div class="bar">www.NovaLink.net.au</div><svg class="wedge" viewBox="0 0 10 5"><polygon points="0,0 10,0 5,5 0,5" fill="#1b3466"/></svg><span class="brand">NOVALINK</span><span class="num">01</span></footer>
</section>

<!-- Headline with two images -->
<section class="page c1 r2">
  <h2 class="page-head">HEADLINE HERE</h2>
  <div class="photo" style="left:26px;top:46px;width:92px;height:116px" role="img" aria-label="Photo of a stressed business owner at his desk"></div>
  <div class="photo" style="left:26px;top:206px;width:92px;height:120px" role="img" aria-label="Photo of a business person reviewing paperwork"></div>
  <div class="page-body" style="left:130px;right:27px">
    <p class="txt lead">Tallyo's mission is to help and support the self-employed and small business owners with their administrative tasks so they can focus on what matters – their business.</p>
    <p class="txt">Administrative tasks are cumbersome, time-consuming and often prevent small owners from focusing their time and energy on their business and their customers. They can also be extremely stressful and nerve-wracking for those attempting these tasks for the first time.</p>
    <p class="txt">At Tallyo, we envisage accounting for the self-employed and small business owners as being <span style="color:var(--accent)">automated and decentralized</span></p>
    <p class="txt">Accounting can and should be done automatically. By connecting to all sources of accounting data such as bank accounts, payment systems, e-commerce websites, and invoicing systems, Tallyo AI automatically completes these tasks, which would take hours to do manually. Bookings are created automatically and fully completed. Financial statements are available within a couple of clicks, and after analysing your data, Tallyo AI will offer you tips to improve your financial stability.</p>
    <p class="txt">What may seem like a pipedream to the millions of self-employed who struggle with</p>
    <p class="sub">The Tallyo model</p>
    <p class="txt">Tallyo is based on an innovative license model that uses Token-as-a-License (TaaL). The token represents lifelong software license for Tallyo solutions. The Pre-ICO token sales will enable Tallyo to complete its development of Tallyo AI to deliver fully automatic bookkeeping.</p>
  </div>
  <footer class="page-foot"><div class="bar">www.NovaLink.net.au</div><svg class="wedge" viewBox="0 0 10 5"><polygon points="0,0 10,0 5,5 0,5" fill="#1b3466"/></svg><span class="brand">NOVALINK</span><span class="num">01</span></footer>
</section>

<!-- Headline with wide image -->
<section class="page c2 r2">
  <h2 class="page-head">HEADLINE HERE</h2>
  <div class="photo" style="left:29px;top:46px;width:209px;height:92px" role="img" aria-label="Photo of a stressed business owner comforted by a colleague"></div>
  <div class="page-body" style="top:144px">
    <p class="txt lead">Tallyo's mission is to help and support the self-employed and small business owners with their administrative tasks so they can focus on what matters – their business.</p>
    <p class="txt">Administrative tasks are cumbersome, time-consuming and often prevent small owners from focusing their time and energy on their business and their customers. They can also be extremely stressful and nerve-wracking for those attempting these tasks for the first time.</p>
    <p class="txt">At Tallyo, we envisage accounting for the self-employed and small business owners as being <span style="color:var(--accent)">automated and decentralized</span></p>
    <p class="txt">Accounting can and should be done automatically. By connecting to all sources of accounting data such as bank accounts, payment systems, e-commerce websites, and invoicing systems, Tallyo AI automatically completes these tasks, which would take hours to do manually. Bookings are created automatically and fully completed. Financial statements are available within a couple of clicks, and after analysing your data, Tallyo AI will offer you tips to improve your financial stability.</p>
    <p class="txt">What may seem like a pipedream to the millions of self-employed who struggle with their admin, is already a reality. Now is the time to join Tallyo on its mission to transform the world of bookkeeping through the power of AI.</p>
    <p class="sub">The Tallyo model</p>
    <p class="txt">Tallyo is based on an innovative license model that uses Token-as-a-License (TaaL). The token represents lifelong software license for Tallyo solutions. The Pre-ICO token sales will enable Tallyo to complete its development of Tallyo AI to deliver fully automatic bookkeeping.</p>
    <p class="txt">with leading edge business data access to ensure you have the best available data at your fingertips.</p>
  </div>
  <footer class="page-foot"><div class="bar">www.NovaLink.net.au</div><svg class="wedge" viewBox="0 0 10 5"><polygon points="0,0 10,0 5,5 0,5" fill="#1b3466"/></svg><span class="brand">NOVALINK</span><span class="num">01</span></footer>
</section>

<!-- Understanding -->
<section class="page c3 r2">
  <h2 class="page-head">OUR UNDERSTANDING OF YOUR NEEDS</h2>
  <div class="page-body" style="top:45px">
    <p class="txt">In the last two weeks of January 2014 we conducted high level conversations both with your staff and your technology partner Ravenstep. As a result of those conversations we've been able to gather the following high level goals for your project:</p>
    <p style="font-size:6px;line-height:1.3;color:#777;margin:5px 0 5px">Cloudrell must be in place to support Tidewise at launch and as the program evolves</p>
    <p class="txt" style="color:var(--accent);font-weight:600">The most critical aspect of this implementation both in terms of time sensitivity as well as functionality is centered around the support for the Tidewise project. Our current understanding of this project and how it relates to Cloudrell is as follows:</p>
    <ul class="bullets">
      <li>Tidewise will be comprised of a series of websites focused on organizing institutions and individuals within six specific community sectors with the goal of increased institutional and public support to help communities become better prepared to minimize the risks and maximize opportunities of a changing climate.</li>
      <li>The primary goals of the CRM application are:
        <ul>
          <li>capture information of individuals and organizations (along with their respective roles)</li>
          <li>track their progress on their site specific to-do lists and site interactions</li>
          <li>allow greenHorizon to push out next steps (ideally in an automated style) related to their to-do list progress and online interactions</li>
          <li>infuse greenHorizon's online and offline marketing program with useful segmentation information</li>
          <li>natively integrate with both the Tidewise family of sites as well as greenHorizon's email service provider of choice</li>
        </ul>
      </li>
      <li>The data architecture must be well defined but flexible to support the core needs of the sites as launch as well as anticipated needs in the future.
        <ul>
          <li>For instance, the faith based site may collect a "denomination" field, while other sites may not collect that field.</li>
          <li>Future interactions outside of the to-do list may become necessary to track and greenHorizon will need a systemic way to capture those interactions, be able to segment on them and potentially provide automated marketing around those similar to the to-do list</li>
        </ul>
      </li>
      <li>The information collected from the Tidewise sites must be combined with current information held within greenHorizon and provide a holistic view of institutions and individuals.</li>
    </ul>
  </div>
  <footer class="page-foot"><div class="bar">www.NovaLink.net.au</div><svg class="wedge" viewBox="0 0 10 5"><polygon points="0,0 10,0 5,5 0,5" fill="#1b3466"/></svg><span class="brand">NOVALINK</span><span class="num">01</span></footer>
</section>

<!-- Budget -->
<section class="page c4 r2">
  <h2 class="page-head">BUDGET AND TIMEFRAME</h2>
  <div class="page-body" style="top:45px">
    <p class="sub" style="margin-top:0">Implementation Estimate</p>
    <p class="txt">The bulk of the implementation costs will be defined by discovery. Based on similar CRM implementation projects, we feel expect that the CRM side will be somewhere between 200 and 300 hours, give or take. The wide swing in hours in phase one is related to the ill-defined nature of both the integration needs and our role in the integration project. Our focus in discovery (as mentioned above) will be to nail down those requirements and our role as it relates to what is needed to integrate the sites with the CRM.</p>
    <table class="grid">
      <tr><th style="width:52%">Task</th><th>Hours</th><th>Cost</th></tr>
      <tr><td>Discovery</td><td>40</td><td>$8,000</td></tr>
      <tr class="phase"><td colspan="3">Phase 1</td></tr>
      <tr><td>Discovery</td><td>20-40</td><td>$8,000</td></tr>
      <tr><td>Discovery</td><td>20-40</td><td>$8,000</td></tr>
      <tr><td>Discovery</td><td>20-40</td><td>$8,000</td></tr>
      <tr class="total"><td>Total Phase 1</td><td>80-240</td><td>$16,800-40,000</td></tr>
      <tr class="phase"><td colspan="3">Phase 2</td></tr>
      <tr><td>Discovery</td><td>20-40</td><td>$8,000</td></tr>
      <tr class="total"><td>Total Phase 2</td><td>80-240</td><td>$16,800-40,000</td></tr>
      <tr class="grand"><td>Total Estimated Implementation Cost</td><td>220-480</td><td>$44,000-96,000</td></tr>
    </table>
    <p class="sub" style="margin-top:8px">Project Timeline</p>
    <p class="txt">Based on the information we have out our disposal, the March 21st launch date doesn't seem a realistic goal to get both the work done needed to provide the foundation for the future CRM instance and the integration given the state of apparent flux of the requirements. That said, we feel it prudent to proceed with discovery before committing to or pushing that date. We are currently estimating that the first phase will take somewhere between 7 and 12 weeks (including discovery) to complete.</p>
    <table class="grid">
      <tr><th style="width:60%">Task</th><th>Weeks to Complete</th></tr>
      <tr><td>Discovery</td><td>1-2</td></tr>
      <tr><td>Phase 1</td><td>6-10</td></tr>
      <tr><td>Phase 2</td><td>8-12</td></tr>
      <tr class="total"><td>Total Number of Weeks</td><td></td></tr>
    </table>
  </div>
  <footer class="page-foot"><div class="bar">www.NovaLink.net.au</div><svg class="wedge" viewBox="0 0 10 5"><polygon points="0,0 10,0 5,5 0,5" fill="#1b3466"/></svg><span class="brand">NOVALINK</span><span class="num">01</span></footer>
</section>

<!-- Solution -->
<section class="page c1 r3">
  <h2 class="page-head">HEADLINE HERE</h2>
  <div class="page-body" style="left:26px;right:27px;top:47px">
    <p class="sub" style="margin-top:0">Solution</p>
    <p class="mini">AI automated accounting</p>
    <p class="txt">Tallyo builds automation in stages on top of its current system to reach full automation thanks to the Tallyo AI. Tallyo AI automates every manual task performed by the user. It starts by connecting to all sources of accounting data such as bank accounts, credit card, webshop or document management systems (Boxwell or Stratavault). Based on these data, Tallyo AI creates bookings and generates financial reports. Finally, Tallyo AI features chat-like interface that allows users to communicate seamlessly with it, viewing it as a trusted advisor over time for all their accounting queries.</p>
    <p class="mini">Blockchain software license or Token-as-a-License (TaaL)</p>
    <p class="txt">It is possible to create tokens on blockchain that represent software licenses, also known as Token-as-a-Licence (TaaL). Tallyo creates TaaL by using the Kelvar official wallet which interacts with the Kelvar blockchain. Upon purchase of TaaL, the token holder is free to transfer or sell TaaL using secondary market that is built directly over the blockchain, in our case, the Kelvar marketplace. Tallyo checks the validity of a token against the blockchain ensuring that token holders have access to the software. TaaL make distribution and securisation of software licenses easier for software developers. It also makes the management and resale of software license easier for software owners. All in all, TaaL has a higher value as a normal software license.</p>
    <p class="sub">Pre-ICO Token sale</p>
    <p class="txt">To realize this innovative vision, Tallyo is launching a pre-ICO in form of a token sale on Kelvar blockchain. 20,000,000 tokens are available to purchase for the price of CHF 0.10 each during a 30-day period to be announced. Tokens represent Tallyo lifelong software licenses and by purchasing enough tokens, holders gain access to Tallyo software. 15,000 tokens give access to Tallyo invoicing or accounting. 20,000 tokens give access to both Tallyo accounting and invoicing. Future customers will still have the opportunity to buy directly yearly or monthly subscriptions to have access to Tallyo.</p>
    <p class="sub">Future plans</p>
    <p class="txt">A future ICO is planned between 18 and 24 months after the pre-ICO token sale. This offering will support the development of Tallyo into a fully decentralized, privacy-focused ecosystem of applications. The new model will reward each participant so that a new world with zero administrative tasks becomes reality.</p>
  </div>
  <footer class="page-foot"><div class="bar">www.NovaLink.net.au</div><svg class="wedge" viewBox="0 0 10 5"><polygon points="0,0 10,0 5,5 0,5" fill="#1b3466"/></svg><span class="brand">NOVALINK</span><span class="num">01</span></footer>
</section>

<!-- Back cover -->
<section class="page c2 r3 back">
  <svg width="259" height="366" viewBox="0 0 259 366">
    <polygon points="0,0 259,0 259,222 0,298" fill="#1b3466"/>
    <polygon points="0,298 259,222 259,258" fill="#6e7987"/>
  </svg>
  <div class="wordmark"><i></i>NOVALINK</div>
  <div class="contact">
    <p>Level 3 18 Cresting Street, Quarry Bay Vic 3999</p>
    <p>4/220 Harlow Street, Ridgeford Victoria 3988</p>
    <p style="margin-bottom:5px">PO Box 902, Ridgeford Victoria 3987</p>
    <p class="line"><span class="dot"></span>1800 555 014</p>
    <p class="line"><span class="dot"></span>info@NovaLink.net.au</p>
    <p class="line"><span class="dot"></span>www.NovaLink.net.au</p>
    <p>ABN 00 000 000 000</p>
  </div>
</section>

</body>
</html>
```